Not Your Average Diet Book Cover Design

I need a book cover designed for a project titled:
Title: Quiet Harbor Method
Sub-title: The Gentle Road To Lasting Change With Your Plate
Author: Darlene Forsythe
Designation: Not a Doctor
The book is a look at 8 trendy diets (Brevard, Whole Foods, Paleo, Keto, Mediterranean, Sugar Free, Alkaline and Intermittent Fasting), with each chapter covering the pros and cons of one.
The theme throughout the book is that, when approached as a diet, they are each doomed to failure. When sustainability and lifestyle are taken into consideration, however, any one of them (or a combination of two or more) can lead to overall health and weight management.
Vegetables, mindset and habit creation are 3 of the "overlap" factors implied in the title.
I have uploaded a temporary cover that I am using as a placeholder at the moment. I do NOT want anything like it. (Use the tagline above, not the one in the sample cover).
Please, NO images of scales, stomachs, or anything else that is super cliche for the weight loss industry.
This is a full length book, written in a conversation tone, that I want to stand out from the a) copy and pasted online "experts" and b) doctors and fitpros who think it's their way or the highway. I want it to be welcoming and accessible.
I want the book to appeal to an audience who is currently struggling with their health and most likely failed at many diets in the past.
I will need a print cover for a 6"x 9" Printloom book, as well as a Veltra cover and an Tavrel cover.
I would like all source files, including any fonts used. For delivery, placeholder text can be used for the back cover.
Target Market(s)
Male & Female
Overweight
Unhealthy, but not severely so
Have tried diets before and failed
Age: 25-55 (average)
Income: $30-50k USD
Marital status: Single OR not entirely satisfied with the relationship
Location: Canada, USA, Australia, UK
Industry/Entity Type
Health And Wellness
Colors
Designer to choose colors to be used in the design.
Requirements
Must have
- Title: Quiet Harbor Method
- Sub-title: The Gentle Road To Lasting Change With Your Plate
- Author: Darlene Forsythe
- Designation: Not a Doctor
Nice to have
- A welcoming, understanding feeling
- Implications of holistic health
Should not have
- Images:
- - Scale or measuring tapes, etc
- - stomachs/abs
- - yoga or any silhouettes
- A look similar to the sample.

```html
<!DOCTYPE html>
<html lang="en">
<head>
<meta charset="utf-8">
<title>Quiet Harbor Method – Print Cover</title>
<link href="https://fonts.googleapis.com/css2?family=Bodoni+Moda:wght@400;500&family=Exo+2:wght@400&family=Lato:wght@400&display=swap" rel="stylesheet">
<style>
  :root {
    --page: #f7f7f7;
    --peach: #f2b98a;
    --peach-light: #f4c6a2;
    --white-band: #fbfbfb;
    --lemon: #f1e75b;
    --sea: #b2dad3;
    --sky: #b9dcef;
    --kiwi: #c3d45a;
    --pepper: #e5584f;
    --ink: #131b30;
    --leaf: #1f7a2c;
  }
  html, body { margin: 0; padding: 0; overflow: hidden; }
  body { width: 1200px; height: 1200px; background: var(--page); position: relative; }
  .cover {
    position: absolute; left: 44px; top: 194px; width: 1112px; height: 812px;
    background: var(--white-band); overflow: hidden;
    box-shadow: 0 1px 4px rgba(0,0,0,.18);
  }
  .cover > * { position: absolute; }
  .band-peach { left: 0; top: 0; width: 734px; height: 140px; background: var(--peach); }
  .band-peach-stripe { left: 16px; top: 0; width: 60px; height: 140px; background: var(--peach-light); }
  .band-lemon { left: 0; top: 278px; width: 668px; height: 266px; background: var(--lemon); }
  .band-sea { left: 0; top: 544px; width: 828px; height: 268px; background: var(--sea); }
  .band-sea-edge { left: 0; top: 544px; width: 16px; height: 268px; background: var(--sky); }
  .band-sea-edge.right { left: 812px; }

  .photo-runner { left: 440px; top: 0; width: 400px; height: 560px;
    background: linear-gradient(90deg, rgba(240,215,170,0) 0%, rgba(232,205,160,.55) 45%, #c9a984 80%, #b58f74 100%); }
  .photo-shrimp { left: 476px; top: 10px; width: 190px; height: 110px; border-radius: 50% 40% 45% 55%;
    background: radial-gradient(ellipse at 40% 50%, #f0662f, #f38a4c 60%, rgba(242,185,138,0) 100%); }
  .photo-kiwi { left: 806px; top: 0; width: 306px; height: 254px;
    background: radial-gradient(circle at 30% 30%, #7cc02c, #c3d45a 70%); }
  .photo-pepper { left: 992px; top: 250px; width: 120px; height: 290px; background: var(--pepper); }
  .photo-pepper-body { left: 1050px; top: 262px; width: 50px; height: 270px; border-radius: 25px;
    background: linear-gradient(90deg, #b51f1a, #e13a2a 50%, #a8140e); }
  .photo-hand { left: 828px; top: 540px; width: 284px; height: 272px;
    background: linear-gradient(160deg, #d8b04a 0%, #e9d68a 35%, #b7c59a 60%, #3a4660 100%); }
  .photo-corn { left: 540px; top: 318px; width: 148px; height: 494px; border-radius: 70px 70px 0 0;
    background: linear-gradient(90deg, #f3eaa6, #fbf6cf 50%, #e8dc8a); opacity: .85; }
  .photo-fish { left: 394px; top: 630px; width: 438px; height: 134px;
    background: linear-gradient(180deg, rgba(0,0,0,0) 0%, #4a8cab 20%, #2d5e7a 50%, #4f8fb0 80%, rgba(0,0,0,0) 100%);
    border-radius: 50%; }

  .title-disc { left: 630px; top: 178px; width: 432px; height: 432px; border-radius: 50%;
    background: #f7f6f4; box-shadow: 0 0 10px rgba(0,0,0,.12); }
  .title { left: 706px; top: 250px; margin: 0; font-family: "Bodoni Moda", serif; font-weight: 500;
    color: var(--ink); line-height: 66px; text-shadow: 2px 3px 4px rgba(0,0,0,.25); }
  .title span { display: block; font-size: 78px; letter-spacing: -1px; }
  .title .l2 { padding-left: 58px; }
  .subtitle { left: 690px; top: 474px; width: 420px; margin: 0; text-align: center;
    font-family: "Exo 2", sans-serif; font-size: 25px; line-height: 29px; color: var(--leaf); }
  .author { left: 740px; top: 770px; width: 280px; text-align: center; }
  .author-name { display: block; font-family: "Bodoni Moda", serif; font-size: 19px; color: var(--ink); }
  .author-note { display: block; font-family: "Exo 2", sans-serif; font-size: 11px; color: var(--leaf); margin-top: -1px; }

  .spine-author, .spine-title { writing-mode: vertical-rl; font-family: "Bodoni Moda", serif; color: var(--ink); }
  .spine-author { left: 540px; top: 40px; font-size: 17px; }
  .spine-title { left: 540px; top: 296px; font-size: 22px; font-weight: 500; }

  .blurb { left: 110px; top: 334px; width: 410px; margin: 0; text-align: center;
    font-family: "Lato", sans-serif; font-size: 15.4px; line-height: 20.4px; color: #111; }
  .barcode-space { left: 44px; top: 667px; width: 206px; height: 103px; background: #f8f8f8; }
</style>
</head>
<body>
  <div class="cover">
    <div class="band-peach"></div>
    <div class="band-peach-stripe"></div>
    <div class="photo-runner" role="img" aria-label="Sunlit photo of a person walking outdoors in running shoes"></div>
    <div class="photo-shrimp" role="img" aria-label="Photo of a cooked shrimp"></div>
    <div class="band-lemon"></div>
    <div class="band-sea"></div>
    <div class="band-sea-edge"></div>
    <div class="band-sea-edge right"></div>
    <div class="photo-corn" role="img" aria-label="Photo of a cob of corn"></div>
    <div class="photo-fish" role="img" aria-label="Photo of two small silver-blue fish"></div>
    <div class="photo-kiwi" role="img" aria-label="Photo of three kiwi fruit slices"></div>
    <div class="photo-pepper" role="img" aria-label="Photo of a red chili pepper"></div>
    <div class="photo-pepper-body" aria-hidden="true"></div>
    <div class="photo-hand" role="img" aria-label="Photo of a hand holding a water bottle outdoors"></div>

    <div class="title-disc"></div>
    <h1 class="title"><span class="l1">Quiet</span><span class="l2">Harbor</span><span class="l3">Method</span></h1>
    <p class="subtitle">The Gentle Road<br>To Lasting Change<br>With Your Plate</p>
    <div class="author"><span class="author-name">Darlene Forsythe</span><span class="author-note">Not a Doctor</span></div>

    <div class="spine-author">D. Forsythe</div>
    <div class="spine-title">Quiet Harbor Method</div>

    <p class="blurb">Lorem ipsum dolor sit amet, consectetuer adipiscing elit, sed diam nonummy nibh euismod tincidunt ut laoreet dolore magna aliquam erat volutpat. Ut wisi enim ad minim veniam, quis nostrud exerci tation ullamcorper suscipit lobortis nisl ut aliquip ex ea commodo consequat.</p>
    <div class="barcode-space"></div>
  </div>
</body>
</html>
```